Package Design - Disposable Face Towel

Hi,

We are needing assistance with graphic design on our box/carton/package.

The attached image that is white is our biggest competitor.

Our brand is "BRIGHT DEW LTD." Please see the logo we uploaded.

Oder we have in mind for front of box:

Logo
LARGE TOWELS
50 Count
Ultra Soft| 100% USDA Bio-Based|100% Eucalyptus Viscose | Vegan
BRIGHTDEWLTD.EXAMPLE

We like medium to dark blue on most of the box, with white and minimal hot pink or salmon. Something that is sharp, modern, and stands out from our competitors.

Box dimensions are: 6.25 x 5.25 x 4.75 inches

This will be 1 of many design projects.

Target Market(s)

Female Beauty Products

Font styles to use
Serif
Sans Serif

Colors
0054AA
0677BA
7BADD7
CADEEF
E8F1F8
EB3D1F
EC4F4E
F09395
F8D3D4
FCEDEE

Requirements
Must have
• Needs to look sharp and modern

```html
<!DOCTYPE html>
<html lang="en">
<head>
<meta charset="utf-8">
<title>Bright Dew Ltd. – Large Towel Carton</title>
<link href="https://fonts.googleapis.com/css2?family=Cormorant+Garamond:wght@500&family=Josefin+Sans:wght@300;400;600&family=Noto+Sans:wght@400;700&display=swap" rel="stylesheet">
<style>
  :root {
    --bg: #d7d7d7;
    --blue: #2b3aa0;
    --blue-deep: #1c237a;
    --band: #e3e5f1;
    --ink: #2a3596;
    --white: #ffffff;
    --label: #ecedee;
    --perf: #b9bed8;
  }
  * { margin: 0; padding: 0; box-sizing: border-box; }
  html, body { width: 1200px; height: 900px; overflow: hidden; }
  body {
    background: var(--bg);
    font-family: "Josefin Sans", sans-serif;
    position: relative;
  }
  .panel {
    position: absolute;
    overflow: hidden;
    box-shadow: 0 10px 30px rgba(0,0,0,0.12);
  }
  .pattern {
    position: absolute; inset: 0;
  }
  .brand {
    font-family: "Cormorant Garamond", serif;
    font-weight: 500;
    color: var(--white);
    letter-spacing: 0.02em;
    line-height: 1;
    white-space: nowrap;
  }

  /* Top panel */
  .panel-top {
    left: 60px; top: 250px; width: 340px; height: 400px;
    background: var(--blue);
  }
  .panel-top .pattern { background: linear-gradient(160deg, #3342a8, #27359a); }
  .panel-top .brand-lockup {
    position: absolute; left: 0; right: 0; top: 150px; text-align: center;
  }
  .panel-top .brand { font-size: 36px; }
  .site-line {
    margin-top: 16px;
    display: flex; align-items: center; justify-content: center; gap: 10px;
    font-family: "Josefin Sans", sans-serif; font-weight: 400;
    font-size: 10px; letter-spacing: 0.3em; color: var(--white);
  }
  .site-line::before, .site-line::after {
    content: ""; width: 34px; height: 1px; background: var(--white); opacity: .8;
  }

  /* Front panel */
  .panel-front {
    left: 430px; top: 250px; width: 340px; height: 400px;
    background: var(--blue);
  }
  .panel-front .pattern { background: linear-gradient(170deg, #3444aa, #26349a); bottom: 150px; }
  .front-band {
    position: absolute; left: 0; right: 0; bottom: 0; height: 150px;
    background: var(--band);
  }
  .perforation { position: absolute; inset: 0; }
  .panel-front .brand {
    position: absolute; left: 0; right: 0; top: 112px; text-align: center; font-size: 30px;
  }
  .front-copy {
    position: absolute; left: 0; right: 0; bottom: 16px; text-align: center; color: var(--ink);
  }
  .product-name { font-weight: 300; font-size: 34px; letter-spacing: 0.01em; line-height: 1; }
  .count { font-weight: 600; font-size: 13px; margin-top: 2px; letter-spacing: .04em; }
  .claims { font-weight: 400; font-size: 9.5px; margin-top: 14px; letter-spacing: .03em; }
  .front-copy .site-line { color: var(--ink); font-size: 8px; letter-spacing: .08em; margin-top: 8px; }
  .front-copy .site-line::before, .front-copy .site-line::after { background: var(--ink); width: 20px; }

  /* Side panel */
  .panel-side {
    left: 800px; top: 250px; width: 340px; height: 400px;
    background: linear-gradient(180deg, #28349a, var(--blue-deep));
  }
  .side-band {
    position: absolute; left: 0; right: 0; bottom: 0; height: 40px; background: var(--band);
  }
  .info-label {
    position: absolute; left: 28px; top: 50px; width: 284px; height: 290px;
    background: var(--label);
    clip-path: polygon(16px 0, calc(100% - 16px) 0, 100% 16px, 100% calc(100% - 16px), calc(100% - 16px) 100%, 16px 100%, 0 calc(100% - 16px), 0 16px);
    padding: 30px 26px 20px;
    color: var(--ink);
    font-family: "Noto Sans", sans-serif;
  }
  .info-label h2 { font-size: 12px; font-weight: 700; letter-spacing: .04em; margin-bottom: 6px; }
  .info-label p { font-size: 9.6px; line-height: 1.32; text-align: justify; }
</style>
</head>
<body>

  <section class="panel panel-top" aria-label="Top panel">
    <div class="pattern" role="img" aria-label="Subtle tonal herringbone pattern in blue"></div>
    <div class="brand-lockup">
      <div class="brand">BRIGHT DEW LTD.</div>
      <div class="site-line">BRIGHTDEWLTD.EXAMPLE</div>
    </div>
  </section>

  <section class="panel panel-front" aria-label="Front panel">
    <div class="pattern" role="img" aria-label="Subtle tonal herringbone pattern in blue"></div>
    <div class="front-band" role="img" aria-label="Pale lavender herringbone pattern band"></div>
    <svg class="perforation" width="340" height="400" viewBox="0 0 340 400" aria-hidden="true">
      <path d="M30 20 H310 V250 Q310 262 298 262 H250 Q238 262 232 274 L226 290 H114 L108 274 Q102 262 90 262 H42 Q30 262 30 250 Z"
            fill="none" stroke="var(--perf)" stroke-width="1.2" stroke-dasharray="5 4"/>
    </svg>
    <div class="brand">BRIGHT DEW LTD.</div>
    <div class="front-copy">
      <div class="product-name">LARGE TOWEL</div>
      <div class="count">50 COUNT</div>
      <div class="claims">ULTRA SOFT | 100% USDA BIO-BASED | 100% EUCALYPTUS VISCOSE | VEGAN</div>
      <div class="site-line">BRIGHTDEWLTD.EXAMPLE</div>
    </div>
  </section>

  <section class="panel panel-side" aria-label="Side panel">
    <div class="side-band" role="img" aria-label="Pale lavender herringbone pattern band"></div>
    <div class="info-label">
      <h2>WHY BRIGHT DEW TOWELS</h2>
      <p>Using clean skin towels is crucial for maintaining healthy and clear skin. Firstly, clean towels help prevent the spread of bacteria, which can cause acne and other skin infections. Secondly, they remove excess oil, dirt, and dead skin cells without reintroducing impurities back onto your skin. Thirdly, clean towels are gentler and less abrasive, reducing the risk of irritation and inflammation. Additionally, using a fresh towel ensures that skincare products are more effectively absorbed, enhancing their benefits. Lastly, maintaining clean towels as part of your skincare routine promotes overall hygiene and fosters a healthier complexion.</p>
    </div>
  </section>

</body>
</html>
```